website design for B&T Electric

A portfolio website for a high end commercial and residential electrical contracting company. The current site bandtelectric.example does not represent the current direction but the images in the gallery give you an idea of the work we do. Current logo will be uploaded shortly but is black text on white background.
Target Market(s)
General Contractors, Residential Home Owners, clients intersted in Voskal home automation.
Industry/Entity Type
Electrician
Coding
Coded - Design and coding required
Number of Pages Required
2 page
Font styles to use
Sans Serif
Colors
Designer to choose colors to be used in the design.
Requirements
Must have
- Portfolio section highlighting different service areas and products (Voskal Dwellsync, etc)

```html
<!DOCTYPE html>
<html lang="en">
<head>
<meta charset="utf-8">
<title>B&amp;T Electric</title>
<link href="https://fonts.googleapis.com/css2?family=Libre+Baskerville:wght@400;700&family=Roboto:wght@400;500;700&display=swap" rel="stylesheet">
<style>
:root{
  --ink:#1c1c1c;
  --muted:#555a60;
  --blue:#0f67c2;
  --orange:#f5a800;
  --white:#ffffff;
  --footer:#16161c;
  --footer-text:#9a9aa3;
  --serif:"Libre Baskerville", Georgia, serif;
  --sans:"Roboto", Arial, sans-serif;
}
*{box-sizing:border-box;margin:0;padding:0}
html,body{width:1200px;height:2546px;overflow:hidden}
body{position:relative;background:var(--white);font-family:var(--sans);color:var(--ink)}

/* header */
.site-header{position:absolute;left:0;top:0;width:1200px;height:78px;background:var(--white)}
.brand{position:absolute;left:88px;top:24px;font-family:var(--sans);font-weight:500;font-size:24px;line-height:30px;color:var(--ink);letter-spacing:0.5px;text-transform:uppercase}
.nav{position:absolute;top:31px;left:0;font-size:13.5px;color:var(--ink)}
.nav span{position:absolute;white-space:nowrap}
.nav .active{color:var(--orange)}
.search-btn{position:absolute;left:1078px;top:24px;width:31px;height:31px;border-radius:50%;background:var(--blue)}
.search-btn svg{position:absolute;left:8px;top:8px}

/* hero */
.hero{position:absolute;left:0;top:78px;width:1200px;height:526px;background:linear-gradient(180deg,#b4874a 0%,#8a5a26 45%,#5a3a1c 75%,#3d2a18 100%)}
.hero-kicker{position:absolute;left:90px;top:196px;font-family:var(--serif);font-size:27px;color:var(--white)}
.hero-title{position:absolute;left:88px;top:232px;font-family:var(--serif);font-weight:700;font-size:46px;color:var(--white);white-space:nowrap}
.hero-btn{position:absolute;left:90px;top:299px;width:148px;height:34px;border-radius:17px;background:var(--blue);color:var(--white);font-size:11.5px;font-weight:500;letter-spacing:.5px;text-align:center;line-height:34px}
.slide-arrow{position:absolute;top:240px;width:29px;height:48px;background:rgba(255,255,255,.25)}
.slide-arrow.next{background:var(--white)}
.slide-arrow svg{position:absolute;left:9px;top:18px}
.scroll-down{position:absolute;left:578px;top:582px;width:44px;height:44px;border-radius:50%;background:var(--white);box-shadow:0 2px 8px rgba(0,0,0,.15)}
.scroll-down svg{position:absolute;left:15px;top:14px}

/* about */
.section-title{font-family:var(--serif);font-weight:700;color:var(--ink)}
.about-title{position:absolute;left:88px;top:760px;font-size:36px}
.rule{position:absolute;height:2px;width:34px;background:var(--orange)}
.about-text{position:absolute;left:88px;top:826px;width:446px;font-size:12.6px;line-height:20px;color:var(--muted)}
.about-dot{position:absolute;left:520px;top:769px;width:16px;height:16px;border-radius:50%;background:#c8c8c8}
.about-link{position:absolute;left:536px;top:777px;width:60px;height:1px;background:#cfcfcf}
.about-ring{position:absolute;left:1010px;top:925px;width:152px;height:152px;border-radius:50%;border:2px dashed var(--orange)}
.about-card{position:absolute;left:596px;top:701px;width:495px;height:331px;background:var(--white);box-shadow:0 6px 24px rgba(0,0,0,.12)}
.about-photo{position:absolute;left:614px;top:684px;width:496px;height:331px;background:linear-gradient(180deg,#6f83a8 0%,#9aa4b7 45%,#b5a982 60%,#7d7468 80%,#9a8f88 100%)}

/* services */
.services{position:absolute;left:0;top:1105px;width:1200px;height:456px;background:var(--blue);color:var(--white)}
.services .section-title{position:absolute;left:0;width:1200px;top:66px;text-align:center;font-size:33px;color:var(--white)}
.services .rule{left:583px;top:121px;background:var(--white)}
.service{position:absolute;top:145px;width:240px;margin-left:-120px;text-align:center}
.service-icon{position:absolute;left:67px;top:0;width:106px;height:106px;border-radius:50%;background:var(--white);border:5px solid #e6eef8}
.service-icon.active{background:var(--orange)}
.service-icon svg{position:absolute;left:33px;top:33px}
.service-stem{position:absolute;left:119px;top:106px;width:2px;height:20px;background:var(--white)}
.service-stem::after{content:"";position:absolute;left:-3px;top:18px;width:8px;height:8px;border-radius:50%;background:var(--white)}
.service-name{position:absolute;left:0;width:240px;top:140px;font-size:15px}
.service-desc{position:absolute;left:0;width:240px;top:163px;font-size:12px;line-height:17px}
.service-btn{position:absolute;left:65px;top:209px;width:110px;height:31px;border:1px solid var(--white);border-radius:16px;font-size:11px;line-height:29px;font-weight:500}
.service-btn.active{background:var(--orange);border-color:var(--orange)}

/* portfolio */
.portfolio-title{position:absolute;left:0;width:1200px;top:1626px;text-align:center;font-size:34px}
.portfolio .rule{left:583px;top:1672px}
.tile{position:absolute;width:246px;height:230px;overflow:hidden}
.tile::after{content:"";position:absolute;left:0;right:0;bottom:0;height:70px;background:linear-gradient(180deg,rgba(0,0,0,0),rgba(0,0,0,.22))}
.tile.featured::after{display:none}
.tile-label{position:absolute;left:16px;bottom:14px;z-index:1;font-size:16.5px;font-weight:500;color:var(--white);text-shadow:0 1px 3px rgba(0,0,0,.5)}
.tile.featured{background:var(--orange)}
.tile.featured .tile-label{text-shadow:none}
.tile-link{position:absolute;left:107px;top:103px;width:32px;height:32px;border-radius:50%;background:var(--white)}
.tile-link svg{position:absolute;left:8px;top:8px}
.tile-caption{position:absolute;left:0;width:246px;top:143px;text-align:center;font-size:11.5px;color:var(--white)}

/* footer */
.site-footer{position:absolute;left:0;top:2245px;width:1200px;height:301px;background:var(--footer);color:var(--white)}
.site-footer .section-title{position:absolute;left:0;width:1200px;top:62px;text-align:center;font-size:34px;color:var(--white)}
.site-footer .rule{left:583px;top:111px}
.contact-icon{position:absolute;top:150px;width:40px;height:40px;border-radius:50%;background:#23232b}
.contact-icon svg{position:absolute;left:11px;top:11px}
.contact-label{position:absolute;top:150px;font-size:13px;font-weight:500}
.contact-value{position:absolute;top:172px;font-size:11.5px;line-height:22px;color:var(--footer-text)}
.copyright{position:absolute;left:0;width:1200px;top:270px;text-align:center;font-size:10.5px;color:var(--footer-text)}
.to-top{position:absolute;left:1135px;top:243px;width:34px;height:34px;border-radius:50%;background:var(--orange)}
.to-top svg{position:absolute;left:11px;top:11px}
</style>
</head>
<body>

<header class="site-header">
  <div class="brand">B&amp;T Electric</div>
  <nav class="nav">
    <span class="active" style="left:660px">Home</span>
    <span style="left:728px">Gallery</span>
    <span style="left:804px">Specialty Services</span>
    <span style="left:947px">About</span>
    <span style="left:1015px">Contact</span>
  </nav>
  <div class="search-btn"><svg width="15" height="15" viewBox="0 0 15 15"><circle cx="6" cy="6" r="4.5" fill="none" stroke="#fff" stroke-width="1.8"/><line x1="9.4" y1="9.4" x2="13.5" y2="13.5" stroke="#fff" stroke-width="1.8"/></svg></div>
</header>

<section class="hero" role="img" aria-label="Sunset over a lakeside pergola with benches and a wind-bent tree">
  <div class="hero-kicker">Welcome To</div>
  <h1 class="hero-title">Landscape Design Ideas</h1>
  <div class="hero-btn">READ THE STORY</div>
  <div class="slide-arrow" style="left:0"><svg width="10" height="12" viewBox="0 0 10 12"><path d="M7 1 2 6l5 5" fill="none" stroke="#fff" stroke-width="2"/></svg></div>
  <div class="slide-arrow next" style="left:1171px"><svg width="10" height="12" viewBox="0 0 10 12"><path d="M3 1l5 5-5 5" fill="none" stroke="#222" stroke-width="2"/></svg></div>
</section>
<div class="scroll-down"><svg width="14" height="16" viewBox="0 0 14 16"><path d="M7 2v11M3 9l4 4 4-4" fill="none" stroke="#444" stroke-width="1.6"/></svg></div>

<section class="about">
  <h2 class="section-title about-title">About Us</h2>
  <div class="rule" style="left:88px;top:810px"></div>
  <p class="about-text">B &amp; T Electric is a full service electrical contracting shop. We offer commercial, residential, light industrial, and agricultural services. We're Voskal Dwellsync and Voskal Motorized Shades certified, as well as an authorized Kestrel Power generator dealer. We've served the Wood River and South Central Idaho area for over 18 years....</p>
  <div class="about-link"></div>
  <div class="about-dot"></div>
  <div class="about-ring"></div>
  <div class="about-card"></div>
  <div class="about-photo" role="img" aria-label="Single-storey company office building with a green roof under a cloudy sky"></div>
</section>

<section class="services">
  <h2 class="section-title">Specialty Services</h2>
  <div class="rule"></div>

  <div class="service" style="left:195px">
    <div class="service-icon"><svg width="30" height="30" viewBox="0 0 30 30"><rect x="10" y="3" width="10" height="24" rx="1.5" fill="none" stroke="#0f67c2" stroke-width="1.6"/><circle cx="15" cy="9" r="1.5" fill="#0f67c2"/><circle cx="15" cy="15" r="1.5" fill="#0f67c2"/><circle cx="15" cy="21" r="1.5" fill="#0f67c2"/></svg></div>
    <div class="service-stem"></div>
    <div class="service-name">Voskal Dwellsync</div>
    <div class="service-desc">We're proudly certified to install Voskal Dwellsync systems Dwellsync ...</div>
    <div class="service-btn">READ MORE</div>
  </div>

  <div class="service" style="left:463px">
    <div class="service-icon active"><svg width="30" height="30" viewBox="0 0 30 30"><rect x="5" y="4" width="20" height="22" fill="none" stroke="#fff" stroke-width="1.6"/><line x1="15" y1="4" x2="15" y2="26" stroke="#fff" stroke-width="1.6"/><line x1="5" y1="15" x2="25" y2="15" stroke="#fff" stroke-width="1.6"/></svg></div>
    <div class="service-stem"></div>
    <div class="service-name">Voskal Veilo Shades</div>
    <div class="service-desc">Voskal Motorized Shades allow you to automatically adjust the natural...</div>
    <div class="service-btn active">READ MORE</div>
  </div>

  <div class="service" style="left:740px">
    <div class="service-icon"><svg width="30" height="30" viewBox="0 0 30 30"><circle cx="10" cy="9" r="5" fill="none" stroke="#0f67c2" stroke-width="1.6"/><path d="M10 14v7c0 3 3 5 6 5h3" fill="none" stroke="#0f67c2" stroke-width="1.6"/><rect x="19" y="20" width="7" height="9" rx="1" fill="none" stroke="#0f67c2" stroke-width="1.6"/></svg></div>
    <div class="service-stem"></div>
    <div class="service-name">LED Lighting</div>
    <div class="service-desc">LED Lighting has rapidly become a functional and affordable...</div>
    <div class="service-btn">READ MORE</div>
  </div>

  <div class="service" style="left:991px">
    <div class="service-icon"><svg width="30" height="30" viewBox="0 0 30 30"><rect x="3" y="9" width="24" height="15" rx="1.5" fill="none" stroke="#0f67c2" stroke-width="1.6"/><rect x="7" y="6" width="4" height="3" fill="#0f67c2"/><rect x="19" y="6" width="4" height="3" fill="#0f67c2"/><path d="M8 16h5M20 14v4M18 16h4" stroke="#0f67c2" stroke-width="1.6"/></svg></div>
    <div class="service-stem"></div>
    <div class="service-name">Emergency Generators</div>
    <div class="service-desc">Never be without power again-protect yourself from frozen pipes...</div>
    <div class="service-btn">READ MORE</div>
  </div>
</section>

<section class="portfolio">
  <h2 class="section-title portfolio-title">Our Portfolio</h2>
  <div class="rule"></div>

  <div class="tile" style="left:88px;top:1700px;background:linear-gradient(160deg,#e6ecef 0%,#b9c4cc 50%,#3f5568 100%)" role="img" aria-label="Glass office tower seen from below"><span class="tile-label">Commercial</span></div>
  <div class="tile" style="left:348px;top:1700px;background:linear-gradient(180deg,#8a8a88 0%,#bcb6ae 45%,#d9d4ce 100%)" role="img" aria-label="Bright bedroom with skylight and white bed"><span class="tile-label">Residential</span></div>
  <div class="tile" style="left:606px;top:1700px;background:linear-gradient(180deg,#7b8fb6 0%,#d79a6a 40%,#6f88a8 60%,#5a3a2a 100%)" role="img" aria-label="Wooden pier over a calm lake at sunset"><span class="tile-label">Landscape</span></div>
  <div class="tile featured" style="left:864px;top:1700px" role="img" aria-label="Standby home generator">
    <div class="tile-link"><svg width="16" height="16" viewBox="0 0 16 16"><path d="M6.5 9.5l3-3M7 4.5l1.5-1.5a2.5 2.5 0 013.5 3.5L10.5 8M9 11.5 7.5 13A2.5 2.5 0 014 9.5L5.5 8" fill="none" stroke="#333" stroke-width="1.6"/></svg></div>
    <div class="tile-caption">Never be without power again...</div>
    <span class="tile-label">Generator</span>
  </div>

  <div class="tile" style="left:88px;top:1943px;background:linear-gradient(180deg,#8d8c88 0%,#d7d3cc 45%,#a89c8c 100%)" role="img" aria-label="Conference room with long table and office chairs"><span class="tile-label">Voskal Shades</span></div>
  <div class="tile" style="left:348px;top:1943px;background:linear-gradient(180deg,#6a3a22 0%,#b86a38 45%,#7a4426 100%)" role="img" aria-label="Warm-lit living room with bar and billiard table"><span class="tile-label">Voskal Dimming</span></div>
  <div class="tile" style="left:606px;top:1943px;background:radial-gradient(circle at 50% 45%,#c98a46 0%,#5a4a3c 25%,#3a3632 70%)" role="img" aria-label="Single hanging filament light bulb"><span class="tile-label">LED Lightining</span></div>
  <div class="tile" style="left:864px;top:1943px;background:linear-gradient(160deg,#dfe3e0 0%,#c3cac6 60%,#9da6a2 100%)" role="img" aria-label="Charger plugged into a wall outlet"><span class="tile-label">Service Calls</span></div>
</section>

<footer class="site-footer">
  <h2 class="section-title">Contact Us</h2>
  <div class="rule"></div>

  <div class="contact-icon" style="left:134px"><svg width="18" height="18" viewBox="0 0 18 18"><path d="M9 17s-6-6-6-10a6 6 0 0112 0c0 4-6 10-6 10z" fill="none" stroke="#0f67c2" stroke-width="1.5"/><circle cx="9" cy="7" r="2" fill="none" stroke="#0f67c2" stroke-width="1.5"/></svg></div>
  <div class="contact-label" style="left:188px">Address</div>
  <div class="contact-value" style="left:188px">218 Harbor Lane PO Box<br>4410 Millbrook, ID 83000.</div>

  <div class="contact-icon" style="left:486px"><svg width="18" height="18" viewBox="0 0 18 18"><rect x="2" y="4" width="14" height="10" fill="none" stroke="#0f67c2" stroke-width="1.5"/><path d="M2 4l7 6 7-6" fill="none" stroke="#0f67c2" stroke-width="1.5"/></svg></div>
  <div class="contact-label" style="left:541px">Email</div>
  <div class="contact-value" style="left:541px">jmarlow@bandtelectric.example<br>rkeller@bandtelectric.example</div>

  <div class="contact-icon" style="left:913px"><svg width="18" height="18" viewBox="0 0 18 18"><path d="M4 2l3 3-2 2c1 2 3 4 5 5l2-2 3 3-2 3C8 16 2 10 1 4z" fill="none" stroke="#0f67c2" stroke-width="1.5"/></svg></div>
  <div class="contact-label" style="left:969px">Phone Number</div>
  <div class="contact-value" style="left:969px">(208) 555-0147</div>

  <div class="copyright">Copyright 2017 | All Right Reserved</div>
  <div class="to-top"><svg width="12" height="12" viewBox="0 0 12 12"><path d="M2 8l4-4 4 4" fill="none" stroke="#fff" stroke-width="1.8"/></svg></div>
</footer>

</body>
</html>
```